KAY VELORE

We need a letterhead design for an Image & Etiquette Consultancy company based in Singapore.

The services we provide are Personal Image Consultation, Image & Etiquette Workshop for schools and corporate.

The design should have our corporate colour as seen in the logo files I have uploaded.

Since our company helps clients with their image, the design should be aesthetically very appealing. It should reflect a very classy & elegant feel.

I will print the letterhead using my printer but most of the time will use it to write letters to my clients therefore the format should include MS Word.

```html
<!DOCTYPE html>
<html lang="en">
<head>
<meta charset="utf-8">
<title>Kay Velore Letterhead</title>
<link rel="stylesheet" href="https://fonts.googleapis.com/css2?family=Exo+2:wght@400;700&family=Open+Sans:wght@400&display=swap">
<style>
  :root {
    --backdrop: #e2e2e0;
    --paper: #ffffff;
    --plum: #2e163b;
    --gold: #c9a227;
    --ink: #3a3a3a;
  }
  * { margin: 0; padding: 0; box-sizing: border-box; }
  html, body {
    width: 1200px; height: 1200px; overflow: hidden;
    background: var(--backdrop);
  }
  .letterhead {
    position: absolute; left: 273px; top: 138px;
    width: 653px; height: 922px;
    background: var(--paper);
    overflow: hidden;
  }
  .brand {
    position: absolute; left: 60px; top: 64px;
    display: flex; align-items: center; gap: 12px;
  }
  .brand-square { width: 40px; height: 40px; background: var(--plum); }
  .brand-name {
    font-family: "Exo 2", sans-serif; font-weight: 400;
    font-size: 36px; letter-spacing: 1px; color: var(--plum);
    line-height: 1;
  }
  .footer-rule {
    position: absolute; left: 0; right: 0; top: 886px;
    height: 2px; background: var(--gold);
  }
  .footer-band {
    position: absolute; left: 0; right: 0; top: 892px; bottom: 0;
    background: var(--plum);
  }
  .company {
    position: absolute; right: 188px; top: 826px; text-align: right;
  }
  .company-name {
    font-family: "Exo 2", sans-serif; font-weight: 700;
    font-size: 14px; letter-spacing: 0.6px; color: var(--plum);
    line-height: 18px; margin-bottom: 4px;
  }
  .company-line {
    font-family: "Open Sans", sans-serif; font-size: 9.5px;
    color: var(--ink); line-height: 16px;
  }
  .contacts { position: absolute; left: 498px; top: 826px; list-style: none; }
  .contacts li {
    display: flex; align-items: center; gap: 7px;
    font-family: "Open Sans", sans-serif; font-size: 9.5px;
    color: var(--ink); line-height: 15.5px;
  }
  .contacts svg { width: 10px; height: 10px; fill: var(--ink); }
</style>
</head>
<body>
  <main class="letterhead">
    <div class="brand">
      <span class="brand-square"></span>
      <span class="brand-name">KAY VELORE</span>
    </div>

    <div class="company">
      <p class="company-name">Kay Velore Limited</p>
      <p class="company-line">Your Long address with code no.</p>
      <p class="company-line">your licence no.: xxx xxx xxx xx</p>
    </div>

    <ul class="contacts">
      <li>
        <svg viewBox="0 0 10 10"><path d="M1,3 C1,1.5 3,1 5,1 C7,1 9,1.5 9,3 L7.5,3.8 L6.8,2.6 L3.2,2.6 L2.5,3.8 Z M2.5,4.5 L7.5,4.5 L8.5,9 L1.5,9 Z"/></svg>
        000 000 000 000
      </li>
      <li>
        <svg viewBox="0 0 10 10"><path d="M0.5,2 L9.5,2 L9.5,8 L0.5,8 Z M1,2.5 L5,5.6 L9,2.5" fill="none" stroke="#3a3a3a" stroke-width="0.9"/><path d="M0.5,2 L5,5.3 L9.5,2 Z"/></svg>
        yourname@kayvelore.com
      </li>
      <li>
        <svg viewBox="0 0 10 10"><circle cx="5" cy="5" r="4.2" fill="none" stroke="#3a3a3a" stroke-width="0.9"/><ellipse cx="5" cy="5" rx="1.8" ry="4.2" fill="none" stroke="#3a3a3a" stroke-width="0.8"/><path d="M0.8,5 L9.2,5" stroke="#3a3a3a" stroke-width="0.8"/></svg>
        www.kayvelore.com
      </li>
    </ul>

    <div class="footer-rule"></div>
    <div class="footer-band"></div>
  </main>
</body>
</html>
```